Flyer Design Project

We need a flyer design for our lock company called 'Marbury Latches'. It will be an A5 flyer delivered to local households advertising the benefits of upgrading their existing door locks to higher security , insurance approved ones.
We have the basic text/layout details and are looking forward to receiving your designs to help in the first stage of our new advertising programme.

Target Market(s)

This flyer is intended for general households.
I will be printing the final flyer as double sided, so it can be the same both sides or different each side depending on layout/content etc. any ideas suggestions will be much appreciated.

Industry/Entity Type

Advertising

Requirements
Must have
• HEADING- Something along the lines of 'Security Update', 'Security News' etc.

1) Basic facts- Every 37 seconds a home somewhere in Britain is burgled. In 70% of these burglaries the offenders gain entry through a door.

SUB HEADING- Who has the keys to your home?

TEXT- Over the years keys are lost, lent, borrowed, duplicated or not even handed over from previous owners and/or tennants.
Not only does this make your home more likely to be burgled it may also mean that your insurance policy will not cover you. As part of your insurance requirements you must have approved locks fitted, if they are not this can invalidate your policy.
Upgrading your homes security by upgrading and ensuring your locks are approved is a simple, cost-effective way to ensure not only your homes security but also your peace of mind.
For a free, no-obligation quotation from your local specialists call Marbury Latches on 01632 960418.

None of this text is essential but, i feel, gets the message across well. If you have other ideas then please feel free to use your own ideas.

At the bottom of the page in small lettering will be;

'Marbury Latches' is a trading name of Marbury Gates ltd. registered company no. 7215968. VAT #.412 3095 71. 14 Fenwick Row, Harrowfield.

Our company uses red normally for our name etc. This is by no means a must have but may help, It would also be beneficial to have some photos etc. to help with the text. Any questions please ask.

Nice to have
• I look forward to receiving your ideas and interpretations, i hope this will lead to working with you on our other future projects.
Yours sincerely
Colin Brantley.

```html
<!DOCTYPE html>
<html lang="en">
<head>
<meta charset="utf-8">
<title>Marbury Latches – Security News</title>
<link rel="stylesheet" href="https://fonts.googleapis.com/css2?family=Rye&family=Sancreek&family=Pinyon+Script&family=Courier+Prime:wght@400;700&display=swap">
<style>
  :root {
    --paper-light: #f3e7c4;
    --paper-mid: #e6d29e;
    --paper-dark: #b99a5c;
    --ink: #1c1611;
    --ink-soft: #3a2f24;
  }
  * { margin: 0; padding: 0; box-sizing: border-box; }
  html, body { width: 847px; height: 1200px; overflow: hidden; background: var(--paper-mid); }
  .flyer {
    position: relative;
    width: 847px; height: 1200px;
    background: radial-gradient(ellipse at 50% 45%, var(--paper-light) 0%, var(--paper-mid) 55%, var(--paper-dark) 100%);
    color: var(--ink);
    overflow: hidden;
  }
  .masthead-name {
    position: absolute; top: 44px; left: 0; width: 100%;
    text-align: center;
    font-family: "Pinyon Script", cursive;
    font-size: 30px; color: var(--ink-soft);
  }
  .rule { position: absolute; height: 0; border-top: 2px solid var(--ink); }
  .rule.double { border-top: 5px double var(--ink); height: 5px; }
  .masthead-title {
    position: absolute; top: 86px; left: 0; width: 100%;
    text-align: center;
    font-family: "Rye", serif; font-weight: 400;
    font-size: 80px; line-height: 1; letter-spacing: 2px;
  }
  .masthead-tagline {
    position: absolute; top: 176px; left: 0; width: 100%;
    text-align: center;
    font-family: "Pinyon Script", cursive;
    font-size: 22px; color: var(--ink-soft);
  }
  .headline {
    position: absolute; left: 0; width: 100%;
    text-align: center;
    font-family: "Sancreek", serif; font-weight: 400;
    line-height: 1;
  }
  .headline-top { top: 240px; font-size: 86px; letter-spacing: 2px; }
  .headline-keys { top: 340px; font-size: 245px; letter-spacing: 4px; }
  .headline-bottom { top: 606px; font-size: 72px; letter-spacing: 2px; }
  .body-col {
    position: absolute;
    font-family: "Courier Prime", monospace;
    font-size: 15px; line-height: 1.22;
    text-align: justify;
  }
  .body-col p { margin-bottom: 11px; }
  .col-left { top: 722px; left: 122px; width: 306px; }
  .col-right { top: 712px; left: 445px; width: 294px; }
  .lead { font-weight: 700; }
  .dotted { border-top: 3px dotted var(--ink); margin: 14px 0; }
  .cta { font-weight: 700; font-size: 15.5px; }
  .footer {
    position: absolute; top: 1118px; left: 122px; width: 613px;
    text-align: center;
    font-family: "Courier Prime", monospace;
    font-size: 11px; line-height: 1.5;
  }
  .footer .diamond { display: inline-block; width: 7px; height: 7px; background: var(--ink); transform: rotate(45deg); margin: 0 8px 1px; vertical-align: middle; }
</style>
</head>
<body>
<main class="flyer">
  <div class="rule double" style="top:64px;left:40px;width:290px"></div>
  <div class="rule double" style="top:64px;left:517px;width:290px"></div>
  <div class="masthead-name">Marbury Latches</div>
  <h1 class="masthead-title">SECURITY NEWS</h1>
  <div class="rule" style="top:174px;left:40px;width:767px"></div>
  <div class="masthead-tagline">Important notice to keep your home safe</div>
  <div class="rule" style="top:206px;left:40px;width:767px"></div>

  <h2 class="headline headline-top">“ WHO HAS THE</h2>
  <div class="headline headline-keys">KEYS</div>
  <div class="headline headline-bottom">TO YOUR HOME? ”</div>

  <section class="body-col col-left">
    <p class="lead">Every 37 seconds, a home in Britain is burgled. In 70% of these burglaries, the offenders gain entry through a door.</p>
    <p>Over the years, keys are lost, lent, borrowed, duplicated or not even handed over from previous owners or tenants. Not only does this make your home more likely to be burgled, it may also mean that your insurance policy will not cover you. As part of your insurance requirements you must have approved locks fitted. If they are not, this can invalidate your policy.</p>
  </section>

  <section class="body-col col-right">
    <p>Upgrading your homes security by ensuring your locks are approved is a simple and cost-effective way to ensure not only your home’s security, but also your peace of mind.</p>
    <div class="dotted"></div>
    <p class="cta">For a free, no-obligation quotation from your local specialists, call Marbury Latches on 01632 960418.</p>
    <div class="dotted"></div>
  </section>

  <footer class="footer">
    <span class="diamond"></span>‘Marbury Latches’ is a trading name of Marbury Gates ltd. registered company no. 7215968. VAT #.412 3095 71. 14 Fenwick Row, Harrowfield.<span class="diamond"></span>
  </footer>
</main>
</body>
</html>
```